THE CANOPY MATE® - INSTALLATION INSTRUCTIONS

We are looking to re-design our installation instructions into a tri-fold brochure. (see attached) I have also included our brochure previously done by Pixel Harbor® for symmetry.

Target Market(s)

The installers of our product

Requirements
Must have
• Must have the installation steps provided in our original disclosure of documents.
Please include the identification of: INSTALLATION INSTRUCTIONS,
Please include the logo provided.

```html
<!DOCTYPE html>
<html lang="en">
<head>
<meta charset="utf-8">
<title>The Canopy Mate® – Installation Instructions</title>
<link href="https://fonts.googleapis.com/css2?family=Arimo:ital,wght@0,400;0,700;1,400;1,700&family=Montserrat:ital,wght@1,800&display=swap" rel="stylesheet">
<style>
  :root {
    --steel-dark: #c4c5c8;
    --steel-light: #f5f5f6;
    --yellow: #fde82b;
    --ink: #111111;
    --body: #262626;
    --brand-red: #e2231a;
    --wall: #d9d3c6;
    --concrete: #c3c0b9;
    --concrete-dark: #a9a6a0;
    --safety-yellow: rgba(246, 214, 30, .55);
    --frame: #ffffff;
  }
  * { box-sizing: border-box; margin: 0; padding: 0; }
  html, body { width: 1200px; height: 928px; overflow: hidden; background: #ffffff; }
  .brochure { position: relative; width: 1200px; height: 928px; font-family: "Arimo", Arial, sans-serif; color: var(--body); }
  .panel { position: absolute; top: 0; height: 928px; }
  .panel--left { left: 0; width: 400px; background: linear-gradient(90deg, var(--steel-dark), var(--steel-light) 45%, var(--steel-dark)); }
  .panel--middle { left: 400px; width: 398px; background: linear-gradient(90deg, var(--steel-dark), var(--steel-light) 50%, var(--steel-dark)); }
  .panel--right { left: 798px; width: 402px; background: linear-gradient(90deg, var(--steel-dark), var(--steel-light) 50%, var(--steel-dark)); }
  .photo {
    position: absolute; border: 2px solid var(--frame);
    background:
      radial-gradient(ellipse 22% 30% at var(--spot, 70% 45%), var(--safety-yellow), transparent 70%),
      linear-gradient(180deg, var(--wall) 0%, var(--wall) 22%, var(--concrete) 30%, var(--concrete-dark) 100%);
    box-shadow: 0 1px 3px rgba(0,0,0,.25);
  }
  .step-tag { position: absolute; height: 40px; background: var(--yellow); font-family: "Montserrat", Arial, sans-serif; font-weight: 800; font-style: italic; font-size: 21px; color: var(--ink); line-height: 40px; padding-left: 22px; clip-path: polygon(6% 0, 100% 0, 94% 100%, 0 100%); z-index: 2; }
  .steps { position: absolute; list-style: none; font-size: 12.6px; line-height: 16px; }
  .steps li { position: relative; padding-left: 18px; margin-bottom: 4px; }
  .steps li::before { content: ""; position: absolute; left: 1px; top: 3px; border-left: 10px solid var(--ink); border-top: 5px solid transparent; border-bottom: 5px solid transparent; }
  .brand { color: var(--brand-red); font-weight: 700; font-style: italic; }
  .note { font-style: italic; }
  b { color: var(--ink); }
</style>
</head>
<body>
<main class="brochure">
  <section class="panel panel--left"></section>
  <section class="panel panel--middle"></section>
  <section class="panel panel--right"></section>

  <div class="photo" style="left:40px;top:52px;width:334px;height:197px;--spot:55% 60%" role="img" aria-label="Two installers measuring the width of a concrete enclosure and marking the centerline"></div>
  <div class="step-tag" style="left:37px;top:40px;width:124px">STEP 1</div>
  <ul class="steps" style="left:40px;top:261px;width:340px">
    <li>Using a tape measure and pencil, measure the width of the enclosure. Divide measurement in half. Be sure to make marks at the front and the rear of the enclosure.</li>
    <li>Snap a line between these two marks. This is your <b>“centerline”</b> of the enclosure.</li>
  </ul>

  <div class="photo" style="left:40px;top:375px;width:334px;height:178px;--spot:25% 45%" role="img" aria-label="Installers marking 10 inches forward from the back wall on the centerline"></div>
  <div class="step-tag" style="left:150px;top:364px;width:132px">STEP 2</div>
  <ul class="steps" style="left:40px;top:565px;width:340px">
    <li>Using the <b>“centerline”</b>, measure from the back wall forward 10” and make a mark.</li>
  </ul>

  <div class="photo" style="left:40px;top:643px;width:334px;height:172px;--spot:-30% -30%" role="img" aria-label="Diagram of the 3-4-5 method for finding a 90 degree angle on the enclosure floor"></div>
  <div class="step-tag" style="left:37px;top:630px;width:124px">STEP 3</div>
  <ul class="steps" style="left:40px;top:830px;width:340px">
    <li>Starting at the 10” mark, use the 3’ - 4’ - 5’ method for finding a 90° angle. Snap through the two points creating a line parallel to the back wall. <span class="note">(See illustration above.)</span></li>
  </ul>

  <div class="photo" style="left:420px;top:47px;width:356px;height:201px;--spot:40% 40%" role="img" aria-label="Installer centering the yellow rear frame on the centerline"></div>
  <div class="step-tag" style="left:523px;top:35px;width:134px">STEP 4</div>
  <ul class="steps" style="left:420px;top:261px;width:360px">
    <li>Using the back of the base plates, install the rear frame of <span class="brand">THE CANOPY MATE™</span> on the line parallel to the back wall and center on perpendicular line (<b>“centerline”</b>).</li>
    <li>Ensure label is facing forward. <span class="note">(See illustration above.)</span></li>
  </ul>

  <div class="photo" style="left:420px;top:373px;width:236px;height:180px;--spot:30% 50%" role="img" aria-label="Drilling a masonry hole through a base plate"></div>
  <div class="photo" style="left:665px;top:373px;width:111px;height:180px;--spot:45% 45%" role="img" aria-label="Installer hammering a sleeve anchor into the base plate"></div>
  <div class="step-tag" style="left:535px;top:362px;width:132px">STEP 5</div>
  <ul class="steps" style="left:420px;top:565px;width:360px">
    <li>Drill (1) 3/4” masonry hole in each base plate.</li>
    <li>Install sleeve anchors using the 10 lb. hammer.</li>
    <li>Snug using adjustable wrench. <span class="note">(See pictures above.)</span></li>
  </ul>

  <div class="photo" style="left:420px;top:643px;width:178px;height:172px;--spot:45% 55%" role="img" aria-label="Two installers attaching the left side frame to the rear frame"></div>
  <div class="photo" style="left:605px;top:643px;width:171px;height:172px;--spot:40% 55%" role="img" aria-label="Two installers attaching the right side frame to the rear frame"></div>
  <div class="step-tag" style="left:523px;top:772px;width:134px">STEP 6</div>
  <ul class="steps" style="left:420px;top:830px;width:360px">
    <li>Install left and right side of <span class="brand">THE CANOPY MATE™</span> by attaching to the rear frame previously installed, using the (2) 5/8” hardened carriage bolts provided.</li>
  </ul>

  <div class="photo" style="left:822px;top:52px;width:339px;height:197px;--spot:50% 30%" role="img" aria-label="Overhead view of the assembled frame with equal measurements from the centerline"></div>
  <div class="step-tag" style="left:820px;top:35px;width:126px">STEP 7</div>
  <ul class="steps" style="left:822px;top:261px;width:345px">
    <li>Using the <b>“centerline”</b>, maintain equal measurements to the base plates. <span class="note">(See illustration above.)</span></li>
  </ul>

  <div class="photo" style="left:822px;top:343px;width:219px;height:180px;--spot:55% 55%" role="img" aria-label="Installers checking front base plates against the centerline"></div>
  <div class="photo" style="left:1048px;top:343px;width:113px;height:180px;--spot:55% 35%" role="img" aria-label="Installer drilling through a front base plate"></div>
  <div class="step-tag" style="left:960px;top:315px;width:132px">STEP 8</div>
  <ul class="steps" style="left:822px;top:532px;width:345px">
    <li>Starting with the front most base plates, drill (1) 3/4” masonry hole in each and install sleeve anchors using 10 lb. hammer.</li>
    <li>Snug using adjustable wrench.</li>
  </ul>

  <div class="photo" style="left:822px;top:643px;width:339px;height:172px;--spot:55% 35%" role="img" aria-label="Installer drilling and anchoring the remaining base plates"></div>
  <div class="step-tag" style="left:820px;top:630px;width:126px">STEP 9</div>
  <ul class="steps" style="left:822px;top:830px;width:345px">
    <li>Proceed to drill and install (1) sleeve anchor in each base plate.</li>
    <li>Ensure to maintain equal measurements off of <b>“centerline”</b>. <span class="note">(See illustration above.)</span></li>
  </ul>
</main>
</body>
</html>
```